Bright Nova Works

We need a professional letter head format for our company. Now we have a logo but need to desing a new logo also. I have uploaded our old logo. Use the color in the logo and design a new one.

Dear Designers , Need to mention "BNW" and please dont use our old LOGO. we need a new catchy one.

```html
<!DOCTYPE html>
<html lang="en">
<head>
<meta charset="UTF-8">
<title>Bright Nova Works – Letterhead</title>
<link href="https://fonts.googleapis.com/css2?family=Arimo:wght@700&family=Source+Sans+3:wght@400;600;700&display=swap" rel="stylesheet">
<style>
  :root {
    --backdrop: #e9e9ea;
    --paper: #ffffff;
    --ink: #3a3d44;
    --ink-dark: #111a2b;
    --navy: #12233a;
    --brand-green: #8dc03f;
    --rule: #2d3f55;
    --sign-tone: #d9dbe0;
  }
  * { margin: 0; padding: 0; box-sizing: border-box; }
  html, body { width: 1200px; height: 1200px; overflow: hidden; }
  body {
    background: var(--backdrop);
    font-family: "Source Sans 3", "Helvetica Neue", Arial, sans-serif;
    color: var(--ink);
  }
  .letterhead {
    position: absolute;
    left: 189px; top: 20px;
    width: 822px; height: 1160px;
    background: var(--paper);
  }
  .brand {
    position: absolute;
    left: 0; right: 0; top: 90px;
    display: flex; align-items: center; justify-content: center; gap: 12px;
  }
  .brand-dot {
    width: 30px; height: 30px; border-radius: 50%;
    background: var(--brand-green);
  }
  .brand-name {
    font-weight: 700; font-size: 24px; letter-spacing: 0.5px;
    color: var(--navy);
  }
  .greeting {
    position: absolute; left: 69px; top: 236px;
    font-family: "Arimo", Arial, sans-serif;
    font-weight: 700; font-size: 18px; color: var(--ink-dark);
  }
  .letter-body {
    position: absolute; left: 69px; top: 284px; width: 688px;
    font-size: 17px; line-height: 21.5px; text-align: justify;
  }
  .letter-body p + p { margin-top: 21.5px; }
  .signature {
    position: absolute; left: 67px; top: 768px;
    width: 126px; height: 44px;
    background: linear-gradient(90deg, var(--sign-tone), #eceef1);
    border-radius: 4px;
  }
  .closing {
    position: absolute; left: 72px; top: 808px;
    font-weight: 600; font-size: 16px; color: var(--ink-dark);
  }
  .footer-rule {
    position: absolute; left: 124px; top: 1100px; width: 575px; height: 1.5px;
    background: linear-gradient(90deg, transparent, var(--rule) 12%, var(--rule) 88%, transparent);
  }
  .footer-contacts {
    position: absolute; left: 0; right: 0; top: 1111px;
    display: flex; justify-content: center; align-items: center; gap: 6px;
    font-size: 13.5px; color: var(--ink-dark);
  }
  .footer-contacts .item { display: inline-flex; align-items: center; gap: 4px; }
  .footer-contacts .web { margin-left: 16px; }
  .footer-contacts svg { width: 11px; height: 11px; fill: var(--ink-dark); }
  .footer-address {
    position: absolute; left: 0; right: 0; top: 1133px;
    text-align: center; font-size: 12px; letter-spacing: 0.2px; color: var(--ink-dark);
  }
</style>
</head>
<body>
  <main class="letterhead">
    <header class="brand">
      <span class="brand-dot"></span>
      <span class="brand-name">Bright Nova Works</span>
    </header>

    <p class="greeting">Dear Mr. Carter,</p>

    <section class="letter-body">
      <p>Lorem Ipsum is simply dummy text of the printing and typesetting industry. Lorem Ipsum has been the industry's standard dummy text ever since the 1500s, when an unknown printer took a galley of type and scrambled it to make a type specimen book. It has survived not only five centuries, but also the leap into electronic typesetting, remaining essentially unchanged.</p>
      <p>The standard chunk of Lorem Ipsum used since the 1500s is reproduced below for those interested. Sections 1.10.32 and 1.10.33 from "de Finibus Bonorum et Malorum" by Cicero are also reproduced in their exact original form, accompanied by English versions from the 1914 translation by H. Rackham</p>
      <p>Lorem Ipsum is simply dummy text of the printing and typesetting industry. Lorem Ipsum has been the industry's standard dummy text ever since the 1500s, when an unknown printer took a galley of type and scrambled it to make a type specimen book. It has survived not only five centuries, but also the leap into electronic typesetting, remaining essentially unchanged. It was popularised in the</p>
      <p>The standard chunk of Lorem Ipsum used since the 1500s is reproduced below for those interested. Sections 1.10.32 and 1.10.33 from "de Finibus Bonorum et Malorum" by Cicero are also reproduced in their exact original form, accompanied by English versions from the 1914 translation by H. Rackham</p>
    </section>

    <div class="signature" role="img" aria-label="Handwritten signature of the sender"></div>
    <p class="closing">Valued customers,</p>

    <footer>
      <div class="footer-rule"></div>
      <div class="footer-contacts">
        <span class="item">
          <svg viewBox="0 0 24 24" aria-hidden="true"><path d="M6.6 10.8a15.1 15.1 0 0 0 6.6 6.6l2.2-2.2c.3-.3.7-.4 1-.2 1.1.4 2.3.6 3.6.6.6 0 1 .4 1 1V20c0 .6-.4 1-1 1C10.6 21 3 13.4 3 4c0-.6.4-1 1-1h3.5c.6 0 1 .4 1 1 0 1.3.2 2.5.6 3.6.1.3 0 .7-.2 1z"/></svg>
          (+945)555-010-200
        </span>
        <span class="item">
          <svg viewBox="0 0 24 24" aria-hidden="true"><path d="M3 6h18v12H3zm2 2v.3l7 4.4 7-4.4V8zm0 2.6V16h14v-5.4l-7 4.4z"/></svg>
          info@brightnovaworks.com
        </span>
        <span class="item web">www.brightnovaworks.com</span>
      </div>
      <p class="footer-address">Po. box 201, Street Name, City Name, Zip Code - 00000</p>
    </footer>
  </main>
</body>
</html>
```